Alaskan medical billing service needs a business card design

We need a business card design for a medical billing service, located in Anchorage, AK. We provide medical claims billing and management to Alaskan medical practices/clinics. We would like to see designs that depict Alaskan Mountain Ranges, or water features, or trees. An outdoorsy feel, perhaps. Not exactly sure.

```html
<!DOCTYPE html>
<html lang="en">
<head>
<meta charset="utf-8">
<title>Business Card Options</title>
<link rel="stylesheet" href="https://fonts.googleapis.com/css2?family=Open+Sans:wght@400;600;700&display=swap">
<style>
  :root {
    --sky-blue: #0a8fcc;
    --leaf-green: #8dc63f;
    --ink-gray: #6b6c6f;
    --paper: #ffffff;
    --backdrop: #ffffff;
  }
  html, body {
    margin: 0;
    padding: 0;
    width: 1200px;
    height: 2208px;
    overflow: hidden;
    background: var(--backdrop);
    font-family: "Open Sans", Arial, sans-serif;
  }
  .sheet { position: relative; width: 1200px; height: 2208px; }
  .card {
    position: absolute;
    left: 46px;
    width: 1095px;
    height: 609px;
    background: var(--paper);
    box-shadow: 0 14px 34px rgba(0,0,0,0.28);
    overflow: hidden;
  }
  .card--one   { top: 46px; }
  .card--two   { top: 812px; }
  .card--three { top: 1573px; }

  .holder {
    position: absolute;
    left: 33px;
    top: 42px;
    color: var(--ink-gray);
    font-size: 29px;
    line-height: 35px;
  }
  .holder p { margin: 0; }
  .holder__name { font-weight: 700; text-transform: uppercase; }
  .holder__role { font-weight: 400; text-transform: uppercase; }
  .card--two .holder__role { padding-left: 76px; }
  .card--three .holder { left: 48px; }
  .card--three .holder__name,
  .card--three .holder__role { text-transform: none; font-size: 28px; }
  .card--three .holder__role { padding-left: 68px; }

  .brand {
    position: absolute;
    left: 59px;
    top: 120px;
    width: 520px;
    text-align: center;
    color: var(--leaf-green);
    font-weight: 600;
  }
  .brand__dot {
    display: block;
    width: 160px;
    height: 160px;
    margin: 0 auto 42px;
    border-radius: 50%;
    background: var(--leaf-green);
  }
  .brand__name {
    font-size: 36px;
    letter-spacing: 1px;
    line-height: 41px;
    text-transform: uppercase;
    margin: 0;
  }

  .contact {
    position: absolute;
    left: 637px;
    top: 214px;
    list-style: none;
    margin: 0;
    padding: 0;
    color: var(--ink-gray);
    font-size: 30px;
    line-height: 33px;
  }
  .contact__item { display: flex; align-items: flex-start; margin-bottom: 38px; }
  .contact__icon {
    width: 40px;
    height: 40px;
    margin-right: 21px;
    flex: none;
    fill: var(--sky-blue);
  }
  .waves { position: absolute; left: 0; top: 0; width: 1095px; height: 609px; }
  .wave--blue { fill: var(--sky-blue); }
  .wave--green { fill: var(--leaf-green); }
</style>
</head>
<body>
<svg width="0" height="0" style="position:absolute" aria-hidden="true">
  <defs>
    <symbol id="icon-home" viewBox="0 0 24 24"><path d="M12 2 1 12h3v10h6v-6h4v6h6V12h3z"/></symbol>
    <symbol id="icon-phone" viewBox="0 0 24 24"><path d="M7 2c1 0 1.5.4 2 1.4l1.3 3c.3.8 0 1.4-.6 1.9L8.3 9.4c1 2.4 2.8 4.4 5 5.7l1.2-1.3c.6-.6 1.2-.8 2-.4l2.9 1.5c.9.5 1.2 1.1 1 2l-.7 2.3c-.3 1-1 1.6-2 1.6C9.6 20.4 3.4 13 3.5 5.6c0-1 .6-2.1 1.6-2.6L7 2z"/></symbol>
    <symbol id="icon-fax" viewBox="0 0 24 24"><path d="M6 2h9l3 3v5H6zM3 11h18v11H3zm3 3v2h3v-2zm5 0v2h3v-2zm5 0v2h2v-2zM6 18v2h3v-2zm5 0v2h3v-2zm5 0v2h2v-2z"/></symbol>
  </defs>
</svg>

<main class="sheet">
  <section class="card card--one">
    <svg class="waves" viewBox="0 0 593 330" preserveAspectRatio="none" aria-hidden="true">
      <path class="wave--blue" d="M0,213 C70,240 150,255 235,262 C150,264 60,260 0,247 Z"/>
      <path class="wave--green" d="M0,252 C120,270 230,270 330,257 C430,244 530,240 593,270 C520,252 430,258 330,270 C220,284 100,287 0,277 Z"/>
      <path class="wave--blue" d="M0,287 C150,302 280,292 380,280 C470,270 540,266 593,276 L593,330 L0,330 Z"/>
    </svg>
    <div class="holder">
      <p class="holder__name">Marla J. Kessler</p>
      <p class="holder__role">Owner</p>
    </div>
    <div class="brand">
      <span class="brand__dot"></span>
      <p class="brand__name">Northfield Claims<br>Group, LLC</p>
    </div>
    <ul class="contact">
      <li class="contact__item"><svg class="contact__icon"><use href="#icon-home"/></svg><span>PO Box 470218<br>Anchorage, AK 99502</span></li>
      <li class="contact__item"><svg class="contact__icon"><use href="#icon-phone"/></svg><span>907-555-0142</span></li>
      <li class="contact__item"><svg class="contact__icon"><use href="#icon-fax"/></svg><span>907-555-0143</span></li>
    </ul>
  </section>

  <section class="card card--two">
    <svg class="waves" viewBox="0 0 593 330" preserveAspectRatio="none" aria-hidden="true">
      <path class="wave--blue" d="M0,213 C70,240 150,255 235,262 C150,264 60,260 0,247 Z"/>
      <path class="wave--green" d="M0,252 C120,270 230,270 330,257 C430,244 530,240 593,270 C520,252 430,258 330,270 C220,284 100,287 0,277 Z"/>
      <path class="wave--blue" d="M0,287 C150,302 280,292 380,280 C470,270 540,266 593,276 L593,330 L0,330 Z"/>
    </svg>
    <div class="holder">
      <p class="holder__name">Marla J. Kessler</p>
      <p class="holder__role">Owner</p>
    </div>
    <div class="brand">
      <span class="brand__dot"></span>
      <p class="brand__name">Northfield Claims<br>Group, LLC</p>
    </div>
    <ul class="contact">
      <li class="contact__item"><svg class="contact__icon"><use href="#icon-home"/></svg><span>PO Box 470218<br>Anchorage, AK 99502</span></li>
      <li class="contact__item"><svg class="contact__icon"><use href="#icon-phone"/></svg><span>907-555-0142</span></li>
      <li class="contact__item"><svg class="contact__icon"><use href="#icon-fax"/></svg><span>907-555-0143</span></li>
    </ul>
  </section>

  <section class="card card--three">
    <svg class="waves" viewBox="0 0 593 330" preserveAspectRatio="none" aria-hidden="true">
      <path class="wave--blue" d="M0,213 C70,240 150,255 235,262 C150,264 60,260 0,247 Z"/>
      <path class="wave--green" d="M0,252 C120,270 230,270 330,257 C430,244 530,240 593,270 C520,252 430,258 330,270 C220,284 100,287 0,277 Z"/>
      <path class="wave--blue" d="M0,287 C150,302 280,292 380,280 C470,270 540,266 593,276 L593,330 L0,330 Z"/>
    </svg>
    <div class="holder">
      <p class="holder__name">Marla J. Kessler</p>
      <p class="holder__role">Owner</p>
    </div>
    <div class="brand">
      <span class="brand__dot"></span>
      <p class="brand__name">Northfield Claims<br>Group, LLC</p>
    </div>
    <ul class="contact">
      <li class="contact__item"><svg class="contact__icon"><use href="#icon-home"/></svg><span>PO Box 470218<br>Anchorage, AK 99502</span></li>
      <li class="contact__item"><svg class="contact__icon"><use href="#icon-phone"/></svg><span>907-555-0142</span></li>
      <li class="contact__item"><svg class="contact__icon"><use href="#icon-fax"/></svg><span>907-555-0143</span></li>
    </ul>
  </section>
</main>
</body>
</html>
```